Copperleaf Motorized Shade Business Card

Hello, we've had our logo made. Now we are looking for a clean and cool looking business card. One side can just be the logo with any design elements that might look good with it. The other side will be Name, Phone Number and Email. There will not be an address on the card.

```html
<!DOCTYPE html>
<html lang="en">
<head>
<meta charset="utf-8">
<title>Copperleaf Motorized Shade Business Card</title>
<link rel="stylesheet" href="https://fonts.googleapis.com/css2?family=Montserrat:wght@400;500;700;800&display=swap">
<style>
  :root {
    --navy: #003b78;
    --sky: #1aa3e8;
    --white: #ffffff;
    --ground: #e9edf1;
    --edge: #b9dcf2;
  }
  * { margin: 0; padding: 0; box-sizing: border-box; }
  html, body { width: 1200px; height: 913px; overflow: hidden; }
  body {
    background: var(--ground);
    font-family: "Montserrat", Arial, sans-serif;
    position: relative;
  }
  .card {
    position: absolute;
    width: 700px;
    height: 400px;
    border-radius: 22px;
    overflow: hidden;
  }
  .card--front {
    left: 80px; top: 40px;
    background: var(--navy);
    box-shadow: 0 3px 0 #002c5c, 0 6px 0 #00264f, 0 12px 24px rgba(0,0,0,.18);
    display: flex; align-items: center; justify-content: center;
  }
  .card--back {
    left: 420px; top: 473px;
    background: var(--white);
    box-shadow: 0 3px 0 var(--edge), 0 6px 0 #a5d1ee, 0 12px 24px rgba(0,0,0,.15);
  }
  .brand {
    display: flex; align-items: center; gap: 16px;
  }
  .brand__mark {
    width: 34px; height: 34px;
    background: var(--sky);
    flex: none;
  }
  .brand__name {
    font-weight: 800;
    font-size: 34px;
    line-height: 1.1;
    text-transform: uppercase;
    letter-spacing: .02em;
    white-space: nowrap;
  }
  .card--front .brand__name { color: var(--white); }
  .card--back .brand {
    position: absolute; left: 40px; top: 176px;
    gap: 14px;
  }
  .card--back .brand__name { color: var(--navy); font-size: 22px; }
  .card--back .brand__mark { width: 26px; height: 26px; }
  .divider {
    position: absolute; left: 380px; top: 80px;
    width: 2px; height: 240px;
    background: var(--navy);
  }
  .contact {
    position: absolute; left: 408px; top: 96px;
    width: 270px;
  }
  .contact__name {
    color: var(--navy);
    font-weight: 800;
    font-size: 22px;
    text-transform: uppercase;
    letter-spacing: .02em;
    white-space: nowrap;
  }
  .contact__role {
    color: var(--sky);
    font-weight: 500;
    font-size: 15px;
    text-transform: uppercase;
    margin-top: 2px;
    margin-bottom: 22px;
  }
  .contact__list { list-style: none; }
  .contact__item {
    display: flex; align-items: center; gap: 12px;
    color: var(--navy);
    font-size: 17px;
    margin-bottom: 10px;
    white-space: nowrap;
  }
  .contact__icon { width: 18px; height: 18px; flex: none; fill: var(--sky); }
</style>
</head>
<body>
  <section class="card card--front" aria-label="Card front">
    <div class="brand">
      <span class="brand__mark"></span>
      <span class="brand__name">Copperleaf<br>Motorized Shade</span>
    </div>
  </section>

  <section class="card card--back" aria-label="Card back">
    <div class="brand">
      <span class="brand__mark"></span>
      <span class="brand__name">Copperleaf<br>Motorized Shade</span>
    </div>
    <div class="divider"></div>
    <div class="contact">
      <p class="contact__name">Daniel Whitcombe</p>
      <p class="contact__role">Director</p>
      <ul class="contact__list">
        <li class="contact__item">
          <svg class="contact__icon" viewBox="0 0 24 24"><path d="M6.6 10.8a15.1 15.1 0 0 0 6.6 6.6l2.2-2.2a1 1 0 0 1 1-.25 11.4 11.4 0 0 0 3.6.57 1 1 0 0 1 1 1V20a1 1 0 0 1-1 1A17 17 0 0 1 3 4a1 1 0 0 1 1-1h3.5a1 1 0 0 1 1 1c0 1.250.2 2.45.57 3.57a1 1 0 0 1-.25 1z"/></svg>
          555 018 4472
        </li>
        <li class="contact__item">
          <svg class="contact__icon" viewBox="0 0 24 24"><path d="M2 5h20v14H2z M2 5l10 8 10-8" fill="none" stroke="#1aa3e8" stroke-width="2"/></svg>
          info@brightfold.com
        </li>
        <li class="contact__item">
          <svg class="contact__icon" viewBox="0 0 24 24"><circle cx="12" cy="12" r="9" fill="none" stroke="#1aa3e8" stroke-width="2"/><path d="M3 12h18M12 3c3 3 3 15 0 18M12 3c-3 3-3 15 0 18" fill="none" stroke="#1aa3e8" stroke-width="1.6"/></svg>
          www.brightfold.com
        </li>
      </ul>
    </div>
  </section>
</body>
</html>
```